Shiatsu & Massage Therapy

I need a business card designed for my Mobile Massage services. The client needs to know that I will be doing house calls.

Shiatsu is a japanese type of bodywork that utilizes the same concepts of acupuncture, with the belief that our vital life energy flows through energetic pathways in the body. I will also offer other massage services.

The business card itself I would like to have a design that is very crisp and not too cluttered. The design should be captivating and convey the message of a connection between the body and soul.

Target Market(s)

My target market are people that are already into holistic services and practices such as fitness, yoga, meditation.

Industry/Entity Type

Massage

Contact Information for Business Card

Corinne Halvaro LMT
6072319058
chalvaro@plumridge-mail.net

Font styles to use
Serif
Script

Colors
b7a5cc
fbf289
33a6d7
33b7a4

Requirements
Must have
• I love the look of the picture I attached, the one of the person meditating. I love how the background is very cosmic and stimulating. If there is any way to combine the graphic of the person massaging another person and that feeling of the other image that would be great. I love yellows, blues and purples. PLEASE do not use all of the images. I really would like a them to be inspiration for your own designs.

```html
<!DOCTYPE html>
<html lang="en">
<head>
<meta charset="utf-8">
<title>Shiatsu &amp; Massage Therapy – Business Cards</title>
<link rel="stylesheet" href="https://fonts.googleapis.com/css2?family=Lobster+Two:ital,wght@1,700&family=Gudea&display=swap">
<style>
  :root {
    --plum: #8a1f78;
    --plum-soft: #a64f97;
    --card: #f7f5f3;
    --card-edge: #ece8e5;
    --skin: #ecd9cc;
    --fabric: #c9c4c8;
    --backdrop: #e4e2e4;
  }
  * { margin: 0; padding: 0; box-sizing: border-box; }
  html, body {
    width: 1200px;
    height: 900px;
    overflow: hidden;
    background: var(--backdrop);
  }
  .canvas {
    width: 1200px;
    height: 900px;
    display: flex;
    flex-direction: column;
    align-items: center;
    justify-content: center;
    gap: 56px;
  }
  .card {
    position: relative;
    width: 660px;
    height: 380px;
    background: radial-gradient(ellipse at 35% 70%, #ffffff 0%, var(--card) 55%, var(--card-edge) 100%);
    overflow: hidden;
    box-shadow: 0 10px 28px rgba(0,0,0,0.18);
  }
  .card__photo {
    position: absolute;
    top: 0;
    right: 0;
    width: 330px;
    height: 170px;
    background:
      linear-gradient(100deg, rgba(247,245,243,1) 0%, rgba(247,245,243,0) 35%),
      linear-gradient(180deg, rgba(247,245,243,0) 60%, rgba(247,245,243,1) 100%),
      linear-gradient(160deg, var(--skin) 0%, #f3e6dc 45%, var(--fabric) 80%, #b9b3b8 100%);
  }
  .card__mark {
    position: absolute;
    width: 150px;
    height: 150px;
    border-radius: 50%;
    background: var(--plum);
  }
  .front .card__mark { left: 80px; top: 95px; }
  .back .card__mark { left: 56px; top: 92px; }

  .front__title {
    position: absolute;
    left: 170px;
    top: 250px;
    font-family: "Lobster Two", cursive;
    font-style: italic;
    font-weight: 700;
    font-size: 44px;
    color: var(--plum-soft);
    white-space: nowrap;
  }
  .front__tagline {
    position: absolute;
    right: 46px;
    top: 306px;
    font-family: "Lobster Two", cursive;
    font-style: italic;
    font-weight: 700;
    font-size: 20px;
    color: var(--plum);
  }

  .back__details {
    position: absolute;
    right: 40px;
    top: 170px;
    text-align: right;
    color: var(--plum);
  }
  .back__name {
    font-family: "Lobster Two", cursive;
    font-style: italic;
    font-weight: 700;
    font-size: 38px;
    line-height: 1.1;
  }
  .back__phone,
  .back__email {
    font-family: "Gudea", sans-serif;
    font-size: 30px;
    line-height: 1.2;
  }
</style>
</head>
<body>
  <main class="canvas">
    <section class="card front" aria-label="Card front">
      <div class="card__photo" role="img" aria-label="Soft photo of a person meditating, hands resting on crossed legs"></div>
      <div class="card__mark" aria-hidden="true"></div>
      <h1 class="front__title">Shiatsu &amp; Massage Therapy</h1>
      <p class="front__tagline">Mobile Massage Service</p>
    </section>

    <section class="card back" aria-label="Card back">
      <div class="card__photo" role="img" aria-label="Soft photo of a person meditating, hands resting on crossed legs"></div>
      <div class="card__mark" aria-hidden="true"></div>
      <div class="back__details">
        <p class="back__name">Corinne Halvaro LMT</p>
        <p class="back__phone">T: 607 231 9058</p>
        <p class="back__email">chalvaro@plumridge-mail.net</p>
      </div>
    </section>
  </main>
</body>
</html>
```